Poster Design - Stand Up Paddle Eco Tour

We need a A3 size poster design (using Adobe Illustrator) for our company's stand up paddle tour. Our tour is on flat water, calm and safe, suitable for all ages and level.

WE provide worldclass SUP boards for our customers. And branded Tovar Helsby life jacket. Our instructors are all well trained and exeprience. Plus they are super friendly. Every paddling trip come with a safety boat.

Please refer to attached files for text and photos.

Our website is www.brimwakeglide.com.sg

IMPORTANT NOTE - The design has to be done in Adobe Illustrator. The winning designer has to submit the working file in Adobe Illustrator.

Target Market(s)

Working adult - 20 - 35 year old

Industry/Entity Type

Tourism

Requirements
Must have
• The project MUST be done in Adobe Illustrator and the winning designer has to submit the artwork to us in Adobe Illustrator format.
Nice to have
• pleasant to look at.

```html
<!DOCTYPE html>
<html lang="en">
<head>
<meta charset="utf-8">
<title>Brimwake Glide – SUP &amp; Eco Tour Poster</title>
<link rel="stylesheet" href="https://fonts.googleapis.com/css2?family=Montserrat:wght@600;700&family=Questrial&display=swap">
<style>
  :root {
    --backdrop: #d9dcdf;
    --paper: #f7f7f7;
    --ink: #2b3440;
    --accent: #1f9ad4;
    --body: #333a42;
  }
  * { box-sizing: border-box; margin: 0; padding: 0; }
  html, body { width: 960px; height: 1200px; overflow: hidden; }
  body {
    background: var(--backdrop);
    display: flex; align-items: center; justify-content: center;
    font-family: "Questrial", sans-serif;
  }
  .poster {
    position: relative;
    width: 800px; height: 1131px;
    background: var(--paper);
    box-shadow: 0 4px 18px rgba(0,0,0,.18);
  }
  .masthead {
    position: absolute; top: 0; left: 0; right: 0; height: 290px;
  }
  .brand {
    position: absolute; left: 48px; top: 120px;
    display: flex; align-items: center; gap: 12px;
    font-family: "Montserrat", sans-serif; font-weight: 700;
    font-size: 30px; color: var(--ink); line-height: 1.1;
  }
  .brand-dot { width: 22px; height: 22px; border-radius: 50%; background: var(--ink); flex: none; }
  .intro { position: absolute; left: 348px; top: 132px; width: 420px; }
  .headline {
    font-family: "Montserrat", sans-serif; font-weight: 700;
    font-size: 22px; line-height: 1.05; color: var(--ink);
    text-transform: uppercase; letter-spacing: -.2px;
  }
  .tagline { margin-top: 6px; font-size: 12.5px; line-height: 1.2; color: var(--accent); }
  .invite {
    margin-top: 8px;
    font-family: "Montserrat", sans-serif; font-weight: 600;
    font-size: 14.5px; color: var(--ink); text-transform: uppercase;
  }
  .hero {
    position: absolute; top: 290px; left: 0; right: 0; height: 400px;
    background: linear-gradient(180deg,
      #5f6a76 0%, #8a8f96 30%, #b7a48c 52%, #e9a85a 60%,
      #6b5142 66%, #2c2a2a 80%, #1a1a1c 100%);
  }
  .details {
    position: absolute; left: 348px; top: 712px; width: 420px;
    color: var(--body);
  }
  .pitch { font-size: 15px; line-height: 1.3; }
  .label {
    margin-top: 10px; font-size: 12px; color: var(--accent); text-transform: uppercase;
  }
  .value { font-size: 16px; line-height: 1.25; color: var(--accent); }
  .value.caps { text-transform: uppercase; }
  .notice { margin-top: 12px; font-size: 14px; text-transform: uppercase; color: var(--ink); }
  .links { list-style: none; margin-top: 6px; }
  .links li {
    display: flex; align-items: center; gap: 6px;
    font-size: 15px; line-height: 1.45; color: var(--accent);
  }
  .links svg { flex: none; }
  .booking { margin-top: 10px; font-size: 14px; text-transform: uppercase; color: var(--ink); }
</style>
</head>
<body>
  <main class="poster">
    <header class="masthead">
      <div class="brand"><span class="brand-dot"></span>Brimwake Glide</div>
      <div class="intro">
        <h1 class="headline">Explore the natural coastal surroundings and waterways of Johor on a SUP adventure touring board</h1>
        <p class="tagline">Our tours are flat-water and appropriate for all ages and levels.<br>We have the best possible service and equipment.</p>
        <p class="invite">Join us for a fun and relaxing day</p>
      </div>
    </header>

    <div class="hero" role="img" aria-label="Photo of three stand up paddlers silhouetted on calm water at sunset with mountains behind"></div>

    <section class="details">
      <p class="pitch">What could be better than a group guided tour?<br>With life vests and a safety boat for our guided tour,<br>you can be assured of a secured environment<br>while you focus on just having fun and creating<br>life's best memories with friends and family.</p>
      <p class="label">Timing:</p>
      <p class="value caps">Morning, afternoon, and sunset session</p>
      <p class="label">Location:</p>
      <p class="value">Selvane River, set off from Teluk Arwan,<br>Port Merin. (next to Pasir Lembut)</p>
      <p class="notice">Contact us for booking. We do not accept walk-in.</p>
      <ul class="links">
        <li>
          <svg width="12" height="12" viewBox="0 0 12 12" aria-hidden="true"><circle cx="6" cy="6" r="5" fill="none" stroke="#2b3440" stroke-width="1.3"/><path d="M1 6h10M6 1c-2 2.5-2 7.5 0 10M6 1c2 2.5 2 7.5 0 10" fill="none" stroke="#2b3440" stroke-width="1"/></svg>
          www.brimwakeglide.com.sg
        </li>
        <li>
          <svg width="12" height="12" viewBox="0 0 12 12" aria-hidden="true"><circle cx="6" cy="6" r="6" fill="#2b3440"/></svg>
          brimwake glide
        </li>
      </ul>
      <p class="booking">Booking contact: booking@brimwakeglide.com.sg</p>
    </section>
  </main>
</body>
</html>
```